brimSTONE corporation pty ltd

Contruction industry
It's a wall and floor tiling business

Industry/Entity Type

Business

Requirements
Must have
• Likes-
- clean and easy to read
- a witty design is always well received
- for it to look reputable in the industry
- a strong and direct presentation
- simple but striking colour selection
Should not have
• Dislikes-
- pls no tacky square tiles to resemble tiling

```html
<!DOCTYPE html>
<html lang="en">
<head>
<meta charset="utf-8">
<title>brimSTONE – Business Card</title>
<link rel="stylesheet" href="https://fonts.googleapis.com/css2?family=Gentium+Book+Plus:wght@700&display=swap">
<style>
  :root {
    --card-light: #c9cdeb;
    --card-mid: #3a4380;
    --card-deep: #111a4a;
    --card-dark: #04060f;
    --text-main: #ffffff;
    --text-shadow: rgba(0, 0, 0, 0.85);
  }
  html, body {
    margin: 0;
    padding: 0;
    width: 1200px;
    height: 686px;
    overflow: hidden;
    background: var(--card-dark);
  }
  .card {
    position: relative;
    width: 1200px;
    height: 686px;
    overflow: hidden;
    font-family: "Gentium Book Plus", Georgia, serif;
    color: var(--text-main);
  }
  .card__backdrop {
    position: absolute;
    inset: 0;
    background:
      radial-gradient(ellipse 520px 420px at 560px 340px,
        var(--card-light) 0%,
        #8d93c4 18%,
        var(--card-mid) 45%,
        var(--card-deep) 72%,
        var(--card-dark) 100%);
  }
  .card__brand {
    position: absolute;
    left: 0;
    width: 1142px;
    top: 78px;
    margin: 0;
    text-align: center;
    font-size: 112px;
    font-weight: 700;
    line-height: 1;
    letter-spacing: 6px;
    color: var(--text-main);
  }
  .card__details {
    position: absolute;
    left: 414px;
    top: 274px;
    margin: 0;
    font-size: 27px;
    font-weight: 700;
    letter-spacing: 2.5px;
    line-height: 41px;
    text-shadow: 1px 1px 2px var(--text-shadow), 0 0 3px var(--text-shadow);
  }
  .card__details p {
    margin: 0;
  }
  .card__company {
    margin-bottom: 41px !important;
  }
</style>
</head>
<body>
  <main class="card">
    <div class="card__backdrop" role="img" aria-label="Glossy dark blue floor tiles lit by a soft central light"></div>
    <h1 class="card__brand">brimSTONE</h1>
    <div class="card__details">
      <p class="card__company">brimSTONE</p>
      <p class="card__name">Dan Hollis</p>
      <p class="card__phone">Mobile - 0400 555 183</p>
      <p class="card__email-label">Email -</p>
      <p class="card__email">dan.hollis@example.com</p>
    </div>
  </main>
</body>
</html>
```